I want ideas sample designs for my book cover

Hello,

We need a book cover designed in flat and 3D Versions. We would like to have jpg and png for final output and include a copy of the PSD for future revisions.

Here are the basic details:

Title: The Harvest Lantern Keepers
Author: Dominic Harwell

Dimensions of book:

Was looking at the Pexo website for dimensions. I thought you may want to go on there and look at the different sizes. I used the 6x9” perfect bound US trade size for my book. You will see that this has a spine width of 0.225”, Cover size of 12.48 x 9.25” and spine begins at 6.125”

If you need background info on the author just to get an idea what he does, please check:

http://DominicHarwell.example

IMPORTANT: Please see attached document for a more detailed info:

Exact Title Of book
Back Cover
Spine Info
Measurements of book and dimension
Examples of book covers
Dominic's photo attached

Thanks,
Rosalind

Industry/Entity Type

Life Coaching

Font styles to use
Serif

Requirements
Must have
• Jpg, png and PSD files
• title
• author
• exact dimensions
• front and back cover
• flat and 3d versions

```html
<!DOCTYPE html>
<html lang="en">
<head>
<meta charset="utf-8">
<title>The Harvest Lantern Keepers – Cover Spread</title>
<link rel="stylesheet" href="https://fonts.googleapis.com/css2?family=Anton&family=Arimo:wght@700&family=Fira+Sans+Extra+Condensed:wght@400&family=Open+Sans:ital,wght@0,400;1,400&display=swap">
<style>
  :root {
    --orange: #f07a22;
    --panel: rgba(122, 176, 226, 0.82);
    --ink: #1b1b1b;
    --white: #ffffff;
    --sky-top: #e3edf4;
    --sky-mid: #a9c4dc;
    --sea-deep: #1f4571;
    --sea-mid: #3d6b9a;
    --figure: #14171c;
    --photo-grey: #cfcfcf;
  }
  * { margin: 0; padding: 0; box-sizing: border-box; }
  html, body { width: 1200px; height: 893px; overflow: hidden; background: #ffffff; }
  .cover {
    position: relative;
    width: 1200px;
    height: 893px;
    overflow: hidden;
    font-family: "Open Sans", sans-serif;
  }
  .cover-photo { position: absolute; inset: 0; }

  /* Back cover */
  .blurb-panel {
    position: absolute;
    left: 22px; top: 26px;
    width: 541px; height: 595px;
    background: var(--panel);
    padding: 25px 13px 0 17px;
    color: var(--ink);
    font-size: 12.6px;
    line-height: 17.6px;
    text-align: justify;
    letter-spacing: -0.15px;
  }
  .blurb-panel p + p { margin-top: 17.6px; }

  .author-photo {
    position: absolute;
    left: 36px; top: 642px;
    width: 156px; height: 160px;
    background: linear-gradient(135deg, #f2f2f2, var(--photo-grey));
  }
  .author-bio {
    position: absolute;
    left: 218px; top: 648px;
    width: 333px;
    font-size: 10.2px;
    line-height: 14.2px;
    color: var(--ink);
    text-align: justify;
    letter-spacing: -0.2px;
  }
  .author-site {
    position: absolute;
    left: 61px; top: 826px;
    font-size: 11px;
    font-style: italic;
    color: var(--white);
  }
  .isbn-box {
    position: absolute;
    left: 326px; top: 804px;
    width: 148px; height: 70px;
    background: var(--white);
    font-size: 8px;
    text-align: center;
    padding-top: 8px;
    color: var(--ink);
  }

  /* Spine */
  .spine-title {
    position: absolute;
    left: 588px; top: 82px;
    writing-mode: vertical-rl;
    font-size: 14.5px;
    letter-spacing: 1.9px;
    color: var(--orange);
    white-space: nowrap;
  }
  .spine-photo {
    position: absolute;
    left: 589px; top: 624px;
    width: 20px; height: 30px;
    background: linear-gradient(#f2f2f2, var(--photo-grey));
  }
  .spine-author {
    position: absolute;
    left: 590px; top: 768px;
    writing-mode: vertical-rl;
    font-size: 13px;
    color: var(--ink);
  }

  /* Front cover */
  .tagline {
    position: absolute;
    left: 646px; top: 76px;
    font-family: "Fira Sans Extra Condensed", sans-serif;
    font-size: 27px;
    line-height: 39px;
    color: var(--ink);
  }
  .front-type { position: absolute; inset: 0; }
</style>
</head>
<body>
<div class="cover">

  <svg class="cover-photo" width="1200" height="893" viewBox="0 0 1200 893" role="img" aria-label="Photograph of a man in a dark suit seen from behind, looking out over a bright ocean with waves under a pale sky">
    <defs>
      <linearGradient id="sea-sky" x1="0" y1="0" x2="0" y2="1">
        <stop offset="0" stop-color="var(--sky-top)"/>
        <stop offset="0.45" stop-color="var(--sky-mid)"/>
        <stop offset="0.52" stop-color="var(--sea-mid)"/>
        <stop offset="0.8" stop-color="var(--sea-deep)"/>
        <stop offset="1" stop-color="#8fb0cc"/>
      </linearGradient>
      <linearGradient id="figure-shade" x1="0" y1="0" x2="1" y2="0">
        <stop offset="0" stop-color="var(--figure)" stop-opacity="0"/>
        <stop offset="0.35" stop-color="var(--figure)" stop-opacity="0.85"/>
        <stop offset="1" stop-color="var(--figure)" stop-opacity="0.95"/>
      </linearGradient>
    </defs>
    <rect width="1200" height="893" fill="url(#sea-sky)"/>
    <rect x="840" y="0" width="360" height="893" fill="url(#figure-shade)"/>
  </svg>

  <section class="blurb-panel">
    <p>This path goes way beyond Entrepreneurism! This is a book for the awakening Entrepreneurs who are building businesses for a better world, affecting generations to come. Bringing you disruptive (in a good way) information, to turn you and your business inside-out for maximum acceleration towards your organisational vision, mission and values.</p>
    <p>There is the potential to have a more meaningful life and business by discovering the symbiotic relationship that exists between all beings. You will be empowered to take your life and business to the next level if you answer the call in this book. It will introduce you to the power of Amazonian plant medicine and other entheogens for improving relationships with yourself, your partner and your family, friends, business associates and Mother Earth.</p>
    <p>An entheogen is defined as ‘a substance (usually from a plant, but not always) that is consumed in order to alter one’s state of consciousness or to act as a catalyst towards encounters with other states of being.’ Plant medicine has been successfully used in South America for thousands of years. This ancient wisdom is helping billionaires, industry icons and entrepreneurs to be better leaders, awakening to its potential for allowing deep examination of the psyche which has the ability to heal, eliminate fears and create a new level of success both personally and professionally.</p>
    <p>Dominic shares his own heart-felt personal experiences and insights gained from working with these substances and the amazing medicine men and women of the Amazon who retain thousands of years of ancient wisdom. He has spent years turning himself inside-out to powerfully transform his own life and business and wants to encourage entrepreneurs to do the same. He believes that if enough people have the opportunity to explore their own consciousness, then together we can make a positive impact on humanity. If you are ready to travel to the fringes and take a journey within, you will discover that you are the missing link you have been looking for. Get ready to expand your consciousness, transform your business and create a new inspiring lifestyle, which will benefit all beings and our beautiful Mother Earth.</p>
  </section>

  <div class="author-photo" role="img" aria-label="Black and white portrait of the author smiling"></div>
  <p class="author-bio">Dominic Harwell is an internationally-renowned entrepreneur, speaker, philanthropist, thought leader and best-selling author. Having played the role of transformational coach, facilitator and spoken to over three million people from twelve different countries, he challenges you in his second book to journey deep within yourself to examine the core of your true nature and how it impacts your entrepreneurial journey. Some of the world biggest game changers, social entrepreneurs, internet marketers and consultants have reported that Dominic’s golden edge is to integrate “purpose with profits” in a way that brings greater meaning to the work they are doing here in the world.</p>
  <p class="author-site">www.DominicHarwell.example</p>
  <div class="isbn-box">ISBN</div>

  <p class="spine-title">The HARVEST LANTERN KEEPERS</p>
  <div class="spine-photo" role="img" aria-label="Small portrait of the author"></div>
  <p class="spine-author">Dominic Harwell</p>

  <p class="tagline">How this<br>ancient wisdom is<br>helping billionaires,<br>industry icons and<br>entrepreneurs to be<br>better leaders,<br>increase impact<br>and leave a legacy</p>

  <svg class="front-type" width="1200" height="893" viewBox="0 0 1200 893">
    <defs>
      <filter id="type-shadow" x="-5%" y="-5%" width="110%" height="120%">
        <feDropShadow dx="2" dy="2" stdDeviation="1.5" flood-color="#000" flood-opacity="0.45"/>
      </filter>
    </defs>
    <g class="book-title" fill="var(--orange)" font-family="Anton, sans-serif" filter="url(#type-shadow)">
      <text transform="translate(686 556) rotate(-90)" font-size="44" textLength="76" lengthAdjust="spacingAndGlyphs">The</text>
      <text x="696" y="560" font-size="122" textLength="468" lengthAdjust="spacingAndGlyphs">HARVEST</text>
      <text x="646" y="664" font-size="122" textLength="518" lengthAdjust="spacingAndGlyphs">LANTERN KEEPERS</text>
    </g>
    <text class="series-line" x="802" y="777" fill="var(--white)" font-family="'Fira Sans Extra Condensed', sans-serif" font-size="24" textLength="360" lengthAdjust="spacingAndGlyphs">From the Best Selling Author of “Awaken”</text>
    <text class="author-name" x="792" y="838" fill="var(--orange)" font-family="Arimo, sans-serif" font-weight="700" font-size="56" textLength="370" lengthAdjust="spacingAndGlyphs" filter="url(#type-shadow)">Dominic Harwell</text>
  </svg>

</div>
</body>
</html>
```